New Law Firm needs a business card design

I need a business card for my new law firm called Fenwick Estates and Trusts. I would like designs to use my logo attached. My firm is new and modern. I like the colors orange, white, grey and black. The design I will chose will be one which uses color well, one which looks impressive, smart and modern.

Target Market(s)

Adults aged 30 to 50 seeking professional advice.

Industry/Entity Type

Law Firm

Requirements
Must have
• My logo which is attached.

Must have a modern font, similar to my logo and draft business card.
Should not have
• Any symbols about law, such as scales etc.

```html
<!DOCTYPE html>
<html lang="en">
<head>
<meta charset="utf-8">
<title>Fenwick Estates and Trusts – Business Card</title>
<link rel="stylesheet" href="https://fonts.googleapis.com/css2?family=Lato:wght@300;400;700&display=swap">
<style>
  :root {
    --bg: #e9e9ea;
    --card: #ffffff;
    --ink: #1c1c1c;
    --grey: #7a7a7c;
    --rule: #d6d6d8;
    --ring: #b9b9bc;
    --orange: #f7931e;
  }
  * { box-sizing: border-box; margin: 0; padding: 0; }
  html, body { width: 1200px; height: 926px; overflow: hidden; }
  body {
    background: var(--bg);
    font-family: "Lato", Arial, sans-serif;
    color: var(--ink);
    position: relative;
  }
  .card {
    position: absolute;
    top: 308px;
    width: 540px;
    height: 310px;
    background: var(--card);
    box-shadow: 0 6px 18px rgba(0,0,0,0.12);
  }
  .card--front { left: 40px; }
  .card--back { left: 620px; }

  /* Front */
  .brand {
    position: absolute;
    left: 34px;
    top: 118px;
    width: 170px;
    display: flex;
    align-items: center;
    gap: 12px;
  }
  .brand__mark {
    flex: 0 0 22px;
    height: 22px;
    border-radius: 50%;
    background: var(--orange);
  }
  .brand__name {
    font-size: 17px;
    font-weight: 300;
    letter-spacing: 1px;
    line-height: 1.25;
    color: var(--grey);
  }
  .divider {
    position: absolute;
    left: 218px;
    top: 70px;
    width: 1px;
    height: 170px;
    background: linear-gradient(to bottom, transparent, var(--rule) 25%, var(--rule) 75%, transparent);
  }
  .contact {
    position: absolute;
    left: 236px;
    top: 84px;
    list-style: none;
    font-size: 15px;
    font-weight: 400;
  }
  .contact li {
    display: flex;
    align-items: flex-start;
    gap: 8px;
    margin-bottom: 9px;
    line-height: 1.25;
  }
  .contact__icon {
    flex: 0 0 19px;
    width: 19px;
    height: 19px;
    border-radius: 50%;
    background: var(--orange);
    display: flex;
    align-items: center;
    justify-content: center;
  }
  .contact__icon svg { width: 11px; height: 11px; fill: #fff; }

  /* Back */
  .frame {
    position: absolute;
    left: 155px;
    top: 40px;
    width: 230px;
    height: 230px;
    border-radius: 50%;
    border: 4px solid var(--ring);
  }
  .holder {
    position: absolute;
    left: 0;
    right: 0;
    top: 128px;
    text-align: center;
  }
  .holder__name {
    font-size: 21px;
    font-weight: 400;
  }
  .holder__name strong { font-weight: 700; }
  .holder__role {
    font-size: 10px;
    color: var(--orange);
    letter-spacing: 0.5px;
    margin-left: 4px;
  }
  .holder__quals {
    margin-top: 5px;
    font-size: 10px;
  }
</style>
</head>
<body>

  <section class="card card--front" aria-label="Card front">
    <div class="brand">
      <span class="brand__mark"></span>
      <span class="brand__name">Fenwick Estates &amp; Trusts</span>
    </div>
    <div class="divider"></div>
    <ul class="contact">
      <li>
        <span class="contact__icon"><svg viewBox="0 0 24 24"><path d="M6.6 10.8a15.1 15.1 0 0 0 6.6 6.6l2.2-2.2a1 1 0 0 1 1-.25 11.4 11.4 0 0 0 3.6.57 1 1 0 0 1 1 1V20a1 1 0 0 1-1 1A17 17 0 0 1 3 4a1 1 0 0 1 1-1h3.5a1 1 0 0 1 1 1c0 1.25.2 2.450.57 3.57a1 1 0 0 1-.25 1z"/></svg></span>
        <span>555 204 1187</span>
      </li>
      <li>
        <span class="contact__icon"><svg viewBox="0 0 24 24"><path d="M6 2h12v5H6zM4 8h16a2 2 0 0 1 2 2v6h-4v6H6v-6H2v-6a2 2 0 0 1 2-2zm4 8v4h8v-4z"/></svg></span>
        <span>555 813 2096</span>
      </li>
      <li>
        <span class="contact__icon"><svg viewBox="0 0 24 24"><path d="M3 4h18v13H3zm2 2v9h14V6zM9 19h6v2H9z"/></svg></span>
        <span>daniel@fenwicktrusts.com.au</span>
      </li>
      <li>
        <span class="contact__icon"><svg viewBox="0 0 24 24"><path d="M12 2a7 7 0 0 0-7 7c0 5 7 13 7 13s7-8 7-13a7 7 0 0 0-7-7zm0 9.5A2.5 2.5 0 1 1 12 6.5a2.5 2.5 0 0 1 0 5z"/></svg></span>
        <span>48 Harbour Lane,<br>Suite #512, Kent House, NY 82417</span>
      </li>
    </ul>
  </section>

  <section class="card card--back" aria-label="Card back">
    <div class="frame"></div>
    <div class="holder">
      <p class="holder__name">Daniel <strong>Ashford</strong><span class="holder__role">. LAWYER</span></p>
      <p class="holder__quals">Dip.Legal Prac, BCom, LLB, Grad Cert Tax.</p>
    </div>
  </section>

</body>
</html>
```